Delwyn's Pressure Washing Services

Starting a pressure washing business on my own in Central Valley California, not too much experience so affordable, I do houses, fences, driveways, cars, trailers, RVs. Planning to make this full-time hoping clientele picks up after having a nice business card. Design doesn't have to be flashy, more to the point, I like simplistic/personable. I do not want something exhausting to look at or with too much going on.

Target Market(s)

Residential, Commercial

Industry/Entity Type

Pressure Washing

Contact Information for Business Card

avalible Services

Font styles to use
Sans Serif

Colors
0054AA
0677BA
7BADD7
CADEEF
E8F1F8
0094D4
00A9DD
6FCCEA
C7EBF8
E9F6FB
00AB8E
00BBA5
67D7C9
C6EFE9
E9F9F6

```html
<!DOCTYPE html>
<html lang="en">
<head>
<meta charset="utf-8">
<title>Delwyn's Pressure Washing Services – Business Card</title>
<link rel="stylesheet" href="https://fonts.googleapis.com/css2?family=League+Spartan:wght@700&family=Poppins:wght@400;500;600&display=swap">
<style>
  :root {
    --blue-deep: #0054AA;
    --blue-mid: #0677BA;
    --blue-soft: #7BADD7;
    --blue-pale: #CADEEF;
    --blue-mist: #E8F1F8;
    --teal: #00AB8E;
    --card-white: #F6F7F8;
    --ink: #2B2F36;
    --stage: #E4E6E8;
  }
  * { margin: 0; padding: 0; box-sizing: border-box; }
  html, body { width: 848px; height: 1200px; overflow: hidden; }
  body {
    background: var(--stage);
    font-family: "Poppins", sans-serif;
    color: var(--ink);
    position: relative;
  }
  .card {
    position: absolute;
    left: 151px;
    width: 547px;
    height: 321px;
    background: var(--card-white);
    overflow: hidden;
  }
  .card--front { top: 245px; }
  .card--back  { top: 633px; }

  .corner { position: absolute; inset: 0; width: 100%; height: 100%; }

  .pattern-area { position: absolute; bottom: 0; }
  .pattern-area--deep { background: linear-gradient(135deg, var(--blue-mid), var(--blue-deep)); }
  .pattern-area--pale { background: linear-gradient(135deg, var(--blue-mist), var(--blue-pale)); }

  /* front */
  .front-deep-left  { left: 0; width: 135px; height: 113px; }
  .front-deep-right { right: 0; width: 135px; height: 113px; }
  .front-pale-left  { left: 135px; width: 100px; height: 60px; }
  .front-pale-right { right: 135px; width: 100px; height: 60px; }

  .brand {
    position: absolute;
    left: 0; right: 0;
    top: 146px;
    text-align: center;
    font-weight: 600;
    color: var(--blue-deep);
  }
  .brand__name { font-size: 32px; line-height: 1.15; }
  .brand__tag { font-size: 18px; line-height: 1.3; }

  /* back */
  .back-deep-right { right: 0; width: 135px; height: 114px; }
  .back-pale-right { right: 135px; width: 100px; height: 70px; }

  .brand-mini {
    position: absolute;
    left: 40px; top: 38px;
    font-weight: 600;
    font-size: 11px;
    line-height: 1.25;
    color: var(--blue-deep);
  }
  .person {
    position: absolute;
    left: 38px; top: 84px;
    font-family: "League Spartan", sans-serif;
    font-weight: 700;
    font-size: 40px;
    letter-spacing: 1.5px;
    line-height: 1;
    color: var(--blue-deep);
    text-transform: uppercase;
  }
  .person__last { color: var(--teal); }
  .role {
    position: absolute;
    left: 40px; top: 130px;
    font-size: 13px;
    letter-spacing: 3px;
    font-weight: 500;
    color: var(--ink);
  }
  .contacts {
    position: absolute;
    left: 36px; top: 164px;
    list-style: none;
  }
  .contacts__item {
    display: flex;
    align-items: center;
    height: 32px;
    font-size: 15.5px;
  }
  .contacts__icon {
    width: 18px; height: 18px;
    border-radius: 50%;
    background: var(--teal);
    margin-right: 12px;
    display: flex; align-items: center; justify-content: center;
    flex-shrink: 0;
  }
  .contacts__icon svg { width: 10px; height: 10px; }
</style>
</head>
<body>

<section class="card card--front" aria-label="Card front">
  <svg class="corner" viewBox="0 0 547 321" aria-hidden="true">
    <polygon points="0,0 114,0 0,214" fill="var(--blue-deep)"/>
    <polygon points="436,0 547,0 547,214" fill="var(--blue-deep)"/>
  </svg>
  <div class="pattern-area pattern-area--pale front-pale-left" role="img" aria-label="Pale blue geometric pattern"></div>
  <div class="pattern-area pattern-area--pale front-pale-right" role="img" aria-label="Pale blue geometric pattern"></div>
  <div class="pattern-area pattern-area--deep front-deep-left" role="img" aria-label="Deep blue geometric pattern"></div>
  <div class="pattern-area pattern-area--deep front-deep-right" role="img" aria-label="Deep blue geometric pattern"></div>
  <div class="brand">
    <div class="brand__name">Delwyn's</div>
    <div class="brand__tag">Pressure Washing Services</div>
  </div>
</section>

<section class="card card--back" aria-label="Card back">
  <svg class="corner" viewBox="0 0 547 321" aria-hidden="true">
    <polygon points="432,0 547,0 547,209" fill="var(--blue-deep)"/>
  </svg>
  <div class="pattern-area pattern-area--pale back-pale-right" role="img" aria-label="Pale blue geometric pattern"></div>
  <div class="pattern-area pattern-area--deep back-deep-right" role="img" aria-label="Deep blue geometric pattern"></div>

  <div class="brand-mini">Delwyn's<br>Pressure Washing Services</div>
  <h1 class="person">Delwyn <span class="person__last">Ortega</span></h1>
  <p class="role">CEO&amp; OWNER</p>
  <ul class="contacts">
    <li class="contacts__item">
      <span class="contacts__icon"><svg viewBox="0 0 10 10"><path d="M2 1l2 2-1 1.2c.6 1.2 1.5 2.1 2.8 2.8L7 6l2 2-1.2 1.5C4.5 9 1 5.5.5 2.2z" fill="#fff"/></svg></span>
      2095550147
    </li>
    <li class="contacts__item">
      <span class="contacts__icon"><svg viewBox="0 0 10 10"><rect x="1" y="2" width="8" height="6" rx="1" fill="#fff"/><path d="M1.5 2.6L5 5.3l3.5-2.7" stroke="var(--teal)" stroke-width="0.9" fill="none"/></svg></span>
      hello@delwynwashes.com
    </li>
    <li class="contacts__item">
      <span class="contacts__icon"><svg viewBox="0 0 10 10" fill="none" stroke="#fff" stroke-width="0.9"><circle cx="5" cy="5" r="3.8"/><ellipse cx="5" cy="5" rx="1.6" ry="3.8"/><path d="M1.2 5h7.6"/></svg></span>
      www.delwynwashes.com
    </li>
    <li class="contacts__item">
      <span class="contacts__icon"><svg viewBox="0 0 10 10"><path d="M5 .8a3 3 0 0 1 3 3c0 2.2-3 5.4-3 5.4S2 6 2 3.8a3 3 0 0 1 3-3z" fill="#fff"/><circle cx="5" cy="3.8" r="1.1" fill="var(--teal)"/></svg></span>
      418 Orchard Ln., Modesto
    </li>
  </ul>
</section>

</body>
</html>
```